New Crumvello Poster

This is for designer Doreen ONLY.<br/><br/>hi doreen,<br/><br/>Hope you are well.<br/>I need to redo my Crumvello combo. <br/>So the layout I want is clean and simple. <br/>Photo is on the left hand side, then combo's details and price.<br/>Same poster size.<br/>Thank you<br/><br/><br/>Pho Combo: 1x Pho + 1x Side + 1x Drinks = $23<br/>Noodle Salad Combo: 1x Noodle Salads + 1x Side + 1x Drinks = $23<br/>Rice Combo: 1x Rice + 1x Side + 1x Drinks = $25<br/>Combo for 2: 2x mains + 1x side + 2x Drinks = $39<br/>Family Combo: 4x mains + 2 sides + 4x Drinks = 79

```html
<!DOCTYPE html>
<html lang="en">
<head>
<meta charset="utf-8">
<title>Crumvello Combos</title>
<link rel="stylesheet" href="https://fonts.googleapis.com/css2?family=Kalam:wght@700&family=Open+Sans:wght@600;800&display=swap">
<style>
  :root {
    --backdrop: #5f7175;
    --board: #2c2c2c;
    --board-light: #353535;
    --photo-bg: #242424;
    --orange: #f7901e;
    --white: #ffffff;
  }
  * { margin: 0; padding: 0; box-sizing: border-box; }
  html, body { width: 1200px; height: 1200px; overflow: hidden; }
  body { background: var(--backdrop); position: relative; }

  .poster {
    position: absolute; left: 208px; top: 46px;
    width: 784px; height: 1108px;
    background: radial-gradient(ellipse at 40% 30%, var(--board-light), var(--board) 70%);
  }

  .title {
    position: absolute; left: 62px; top: 66px;
    font-family: "Kalam", cursive; font-weight: 700;
    color: var(--white); line-height: 0.86; transform: skewX(-4deg);
  }
  .title-main { display: block; font-size: 74px; letter-spacing: 1px; }
  .title-sub { display: block; font-size: 54px; margin-top: 2px; }

  .brand {
    position: absolute; left: 620px; top: 74px;
    width: 100px; height: 100px;
    display: flex; align-items: center; justify-content: center;
  }
  .brand-ring { position: absolute; inset: 0; }
  .brand-name {
    position: relative;
    font-family: "Open Sans", sans-serif; font-weight: 800;
    font-size: 16px; color: var(--white); letter-spacing: 1px;
  }

  .combo-list { position: absolute; left: 62px; top: 200px; width: 671px; }
  .combo { display: flex; height: 156px; margin-bottom: 16px; }
  .combo-photo { width: 265px; height: 100%; background: var(--photo-bg); }
  .combo-info {
    flex: 1; background: var(--orange);
    display: flex; align-items: center; justify-content: space-between;
    padding: 0 19px 0 11px;
    font-family: "Open Sans", sans-serif; color: var(--white);
  }
  .combo-name { font-size: 25px; font-weight: 800; line-height: 1.05; letter-spacing: 0.2px; white-space: nowrap; }
  .combo-parts { font-size: 15px; font-weight: 600; margin-top: 3px; letter-spacing: 0.2px; white-space: nowrap; }
  .combo-parts b { font-weight: 800; }
  .combo-price { font-size: 31px; font-weight: 800; }
</style>
</head>
<body>
  <main class="poster">
    <h1 class="title">
      <span class="title-main">CRUMVELLO</span>
      <span class="title-sub">COMBOS</span>
    </h1>

    <div class="brand">
      <svg class="brand-ring" viewBox="0 0 100 100" aria-hidden="true">
        <circle cx="50" cy="50" r="48" fill="none" stroke="#ffffff" stroke-width="1.5"/>
      </svg>
      <span class="brand-name">LUNORA</span>
    </div>

    <section class="combo-list">
      <article class="combo">
        <div class="combo-photo" role="img" aria-label="Pho bowl with a side plate and a bottled iced tea"></div>
        <div class="combo-info">
          <div>
            <h2 class="combo-name">PHỞ COMBO</h2>
            <p class="combo-parts"><b>1x</b> PHỞ + <b>1x</b> SIDE + <b>1x</b> DRINKS</p>
          </div>
          <span class="combo-price">$23</span>
        </div>
      </article>

      <article class="combo">
        <div class="combo-photo" role="img" aria-label="Noodle salad bowl with rice paper rolls, dipping sauce and a bottled drink"></div>
        <div class="combo-info">
          <div>
            <h2 class="combo-name">NOODLE SALAD COMBO</h2>
            <p class="combo-parts"><b>1x</b> NOODLE SALAD + <b>1x</b> SIDE + <b>1x</b> DRINKS</p>
          </div>
          <span class="combo-price">$23</span>
        </div>
      </article>

      <article class="combo">
        <div class="combo-photo" role="img" aria-label="Rice plate with stir-fry, spring rolls and a bottled drink"></div>
        <div class="combo-info">
          <div>
            <h2 class="combo-name">RICE COMBO</h2>
            <p class="combo-parts"><b>1x</b> RICE + <b>1x</b> SIDE + <b>1x</b> DRINKS</p>
          </div>
          <span class="combo-price">$25</span>
        </div>
      </article>

      <article class="combo">
        <div class="combo-photo" role="img" aria-label="Two main dishes, spring rolls and two bottled drinks"></div>
        <div class="combo-info">
          <div>
            <h2 class="combo-name">COMBO FOR 2</h2>
            <p class="combo-parts"><b>2x</b> MAINS + <b>1x</b> SIDE + <b>2x</b> DRINKS</p>
          </div>
          <span class="combo-price">$39</span>
        </div>
      </article>

      <article class="combo">
        <div class="combo-photo" role="img" aria-label="Four main dishes, two sides and four bottled drinks"></div>
        <div class="combo-info">
          <div>
            <h2 class="combo-name">FAMILY COMBO</h2>
            <p class="combo-parts"><b>4x</b> MAINS + <b>2x</b> SIDES + <b>4x</b> DRINKS</p>
          </div>
          <span class="combo-price">$79</span>
        </div>
      </article>
    </section>
  </main>
</body>
</html>
```